Webdesign für Hunde- und Katzenernährungsberatung
Zielgruppe
Hunde und Katzenernährungsberatung, für Menschen, die auch bei ihren Hunden und Katzen auf gesunde, natürliche Ernährung achten wollen, ohne unnötigen Geschmacksverstärker, Zucker, Zusatzstoffe, etc. die gesundheitliche Probleme bei den Tieren verursachen können.
Umstellung auf natürliche, artgerechte Fütterung, teils roh, teils gekocht, angepasst auf Grösse, Rasse, Alter etc., auch speziell für Welpen
Beratung bei:
Übergewicht
Allergien
Unverträglichkeiten
Magen-Darm Problemen
individuelle Ernährungspläne
Selbsthergestellte Kekse, Leckerlies, Snacks, Pralinen und div. Hausmannskost in Einmachgläsern (alles auf Vorbestellung).
Diverse Accessoires
Halsbänder, Leinen, Geschirr aus div. natürlichen Materialien
Lern- und Spielzeug aus Holz und Stoff
div. Zubehör für Tiere, sowie auch für Frauchen und Herrchen
Aufgabenstellung
Die Seite sollte stilvoll aber nicht überfüllt sein und im Retro/Vintage Stil gehalten werden, da das Logo bereits sehr wirksam und eher auffällig ist, dezente Töne im Hintergrund, die Nahrungsmittel werden dann ev. auf Schieferplatten oder unauffälligem Hintergrund platziert. Ich sollte zu einem späteren Zeitpunkt selber Fotos, Links, Texte, etc. einfach dazu fügen können.

```html
<!DOCTYPE html>
<html lang="de">
<head>
<meta charset="utf-8">
<title>PKM – Ernährungsberatung für Hunde und Katzen</title>
<link rel="stylesheet" href="https://fonts.googleapis.com/css2?family=Kaushan+Script&family=Montserrat:wght@500;600&family=Open+Sans:ital@1&display=swap">
<style>
  :root {
    --sky: #95c4de;
    --sky-deep: #6f9fba;
    --cocoa: #4a2410;
    --white: #ffffff;
    --paper: #f4f4f6;
    --apricot: #f5a646;
    --ink: #3e3e3e;
  }
  * { box-sizing: border-box; margin: 0; padding: 0; }
  html, body { width: 1200px; height: 800px; overflow: hidden; background: var(--paper); }
  body { font-family: "Montserrat", sans-serif; color: var(--ink); }
  .page { position: relative; width: 1200px; height: 800px; background: var(--sky); overflow: hidden; }

  .site-header {
    position: absolute; top: 0; left: 0; width: 1200px; height: 80px;
    background: var(--white); display: flex; align-items: center; justify-content: space-between;
    padding: 0 60px; border-top: 5px solid var(--sky);
  }
  .brand { display: flex; align-items: center; gap: 12px; }
  .brand-dot { width: 38px; height: 38px; border-radius: 50%; background: var(--sky); }
  .brand-name { font-family: "Montserrat", sans-serif; font-weight: 600; font-size: 30px; color: var(--sky-deep); letter-spacing: 3px; }
  .menu-toggle { width: 40px; }

  .hero { position: absolute; top: 80px; left: 0; width: 1200px; height: 390px; }
  .hero-copy { position: absolute; left: 60px; top: 40px; width: 560px; text-align: center; }
  .rule { height: 4px; background: var(--white); border-radius: 2px; width: 300px; margin: 0 auto; opacity: .9; }
  .hero-title { font-family: "Kaushan Script", cursive; font-weight: 400; line-height: 0.95; margin: 14px 0 10px; }
  .hero-title .line-one { display: block; color: var(--cocoa); font-size: 66px; }
  .hero-title .line-two { display: block; color: var(--white); font-size: 66px; }
  .hero-sub { font-size: 13px; font-weight: 500; color: var(--cocoa); letter-spacing: .2px; margin-bottom: 14px; }
  .btn {
    display: inline-block; background: var(--sky-deep); color: var(--white);
    font-size: 13px; font-weight: 600; padding: 10px 36px; margin-top: 34px; text-decoration: none;
  }
  .hero-art { position: absolute; right: 60px; top: 30px; width: 460px; height: 350px;
    background: linear-gradient(135deg, #f5a646 0%, #f0b36a 45%, #7a3a1c 46%, #5a2a14 100%); border-radius: 8px; }
  .floor { position: absolute; left: 0; top: 470px; width: 1200px; height: 12px; background: var(--apricot); }

  .shop { position: absolute; top: 482px; left: 0; width: 1200px; height: 318px; background: var(--sky); }
  .shop-photo { position: absolute; left: 60px; top: 28px; width: 400px; height: 262px;
    background: linear-gradient(160deg, #e9d2b0 0%, #b8884f 55%, #8a6236 100%); border-radius: 8px; }
  .shop-copy { position: absolute; left: 510px; top: 30px; width: 620px; color: var(--white); }
  .shop-text { font-family: "Open Sans", sans-serif; font-style: italic; font-size: 13px; line-height: 1.6; }
  .shop-title { font-family: "Kaushan Script", cursive; font-weight: 400; font-size: 28px; margin: 14px 0 8px; }
  .shop-list { list-style: none; }
  .shop-list li { display: flex; align-items: center; gap: 8px; font-size: 12px; font-weight: 600; letter-spacing: .3px; margin: 5px 0; }
  .shop-copy .btn { margin-top: 14px; font-size: 12px; padding: 9px 34px; }
</style>
</head>
<body>
<div class="page">
  <header class="site-header">
    <div class="brand">
      <span class="brand-dot"></span>
      <span class="brand-name">PKM</span>
    </div>
    <svg class="menu-toggle" viewBox="0 0 40 14" aria-label="Menü">
      <rect y="0" width="40" height="2" fill="#6f9fba"/>
      <rect y="6" width="40" height="2" fill="#6f9fba"/>
      <rect y="12" width="40" height="2" fill="#6f9fba"/>
    </svg>
  </header>

  <section class="hero">
    <div class="hero-copy">
      <div class="rule"></div>
      <h1 class="hero-title">
        <span class="line-one">Lorem ipsum</span>
        <span class="line-two">dolor sit amet</span>
      </h1>
      <p class="hero-sub">LOREM IPSUM DOLOR SIT AMET CONSECTETUR ADIPISCING ELIT</p>
      <div class="rule"></div>
      <a class="btn" href="#">ONLINE SHOP</a>
    </div>
    <div class="hero-art" role="img" aria-label="Illustration einer lächelnden orangen Katze und eines braunen Hundes auf blauem Pfotenmuster"></div>
  </section>
  <div class="floor"></div>

  <section class="shop">
    <div class="shop-photo" role="img" aria-label="Foto eines kleinen Hundes mit Futternapf im Maul und Hundekeksen in Knochenform"></div>
    <div class="shop-copy">
      <p class="shop-text">Lorem ipsum dolor sit amet, consectetur adipiscing elit, sed do eiusmod tempor incididunt ut labore et dolore magna aliqua. Ut enim ad minim veniam, quis nostrud exercitation ullamco laboris nisi ut aliquip ex ea commodo consequat. Duis aute irure dolor in reprehenderit in voluptate velit esse cillum dolore eu fugiat nulla pariatur.</p>
      <h2 class="shop-title">Sie können in unserem Online-Shop</h2>
      <ul class="shop-list">
        <li><svg width="14" height="12" viewBox="0 0 14 12"><path d="M1 6 L5 10 L13 1" fill="none" stroke="#fff" stroke-width="2"/></svg>SELBSTHERGESTELLTE KEKSE</li>
        <li><svg width="14" height="12" viewBox="0 0 14 12"><path d="M1 6 L5 10 L13 1" fill="none" stroke="#fff" stroke-width="2"/></svg>LECKERLIES</li>
        <li><svg width="14" height="12" viewBox="0 0 14 12"><path d="M1 6 L5 10 L13 1" fill="none" stroke="#fff" stroke-width="2"/></svg>SNACKS</li>
        <li><svg width="14" height="12" viewBox="0 0 14 12"><path d="M1 6 L5 10 L13 1" fill="none" stroke="#fff" stroke-width="2"/></svg>PRALINEN</li>
        <li><svg width="14" height="12" viewBox="0 0 14 12"><path d="M1 6 L5 10 L13 1" fill="none" stroke="#fff" stroke-width="2"/></svg>DIV. HAUSMANNSKOST IN EINMACHGLÄSERN</li>
      </ul>
      <a class="btn" href="#">MEHR INFOS</a>
    </div>
  </section>
</div>
</body>
</html>
```